Redesign Event Flyer for Speaker

We are re-designing our professional event flyer template with new headshot and cleaner, up-to-date design. All design details are in PDF file attached. Thank you for participating :)

Font styles to use
Sans Serif

Colors
3276b5
0355a3

Requirements
Must have
• All elements in PDF file.
Nice to have
Should not have
• Tacky or childish elements.

```html
<!DOCTYPE html>
<html lang="en">
<head>
<meta charset="utf-8">
<title>The Greatest Sale — Event Flyer</title>
<link rel="stylesheet" href="https://fonts.googleapis.com/css2?family=Bebas+Neue&family=Cinzel:wght@700&family=Oswald:wght@300;600&display=swap">
<style>
  :root {
    --blue-deep: #0355a3;
    --blue-mid: #3276b5;
    --blue-glow: #1a8fd0;
    --white: #ffffff;
    --portrait-dark: #141414;
    --portrait-light: #4a4a4a;
  }
  * { margin: 0; padding: 0; box-sizing: border-box; }
  html, body {
    width: 1200px; height: 848px; overflow: hidden;
    background: var(--blue-deep);
  }
  .flyer {
    position: relative; width: 1200px; height: 848px; overflow: hidden;
    background: radial-gradient(circle at 600px 440px, var(--blue-glow) 0, var(--blue-mid) 200px, var(--blue-deep) 470px);
    color: var(--white);
  }
  .portrait {
    position: absolute; left: 260px; top: 30px; width: 681px; height: 818px;
    border-radius: 300px 300px 0 0;
    background: linear-gradient(180deg, var(--portrait-light) 0%, var(--portrait-dark) 55%, var(--portrait-dark) 100%);
  }
  .brand {
    position: absolute; right: 65px; top: 44px;
    display: flex; align-items: center; gap: 10px;
    font-family: "Oswald", sans-serif; font-weight: 600; font-size: 36px;
    line-height: 1;
  }
  .brand-dot { width: 28px; height: 28px; border-radius: 50%; background: var(--white); }
  .headline {
    position: absolute; left: 211px; top: 432px;
    font-family: "Bebas Neue", sans-serif; font-weight: 400;
    font-size: 168px; line-height: 138px; letter-spacing: 1px;
  }
  .headline-outline {
    color: transparent; -webkit-text-stroke: 2px var(--white);
  }
  .speaker {
    position: absolute; left: 220px; top: 724px;
    font-family: "Cinzel", serif; font-weight: 700; font-size: 19px; letter-spacing: 1.5px;
  }
  .details {
    position: absolute; left: 64px; top: 772px; right: 65px; height: 50px;
    display: flex; align-items: center;
    font-family: "Oswald", sans-serif; font-weight: 300; font-size: 18px; line-height: 21px;
    text-transform: uppercase;
  }
  .detail { display: flex; align-items: center; }
  .detail svg { flex: none; }
  .detail-venue svg { margin-right: 20px; }
  .detail-date svg, .detail-web svg { margin-right: 14px; }
  .divider { width: 1.5px; height: 24px; background: var(--white); margin: 0 18px; }
</style>
</head>
<body>
<div class="flyer">
  <div class="portrait" role="img" aria-label="Black-and-white headshot of the speaker in a dark suit jacket and white open-collar shirt"></div>

  <div class="brand"><span class="brand-dot"></span><span class="brand-name">Brightmark</span></div>

  <h1 class="headline">THE<br>GREATEST <span class="headline-outline">SALE</span></h1>

  <p class="speaker">MARCUS ADRIAN HOLLIS</p>

  <div class="details">
    <div class="detail detail-venue">
      <svg width="24" height="38" viewBox="0 0 24 38" fill="none" stroke="#fff" stroke-width="2">
        <path d="M12 36 C5 24 2 18 2 12 A10 10 0 0 1 22 12 C22 18 19 24 12 36 Z"/>
        <circle cx="12" cy="12" r="5"/>
      </svg>
      <span>Cascade Ridge Golf Club<br>4200 Lakeshore Pkwy, Riverton, Canada</span>
    </div>
    <span class="divider"></span>
    <div class="detail detail-date">
      <svg width="26" height="26" viewBox="0 0 26 26" fill="none" stroke="#fff" stroke-width="1.6">
        <rect x="2" y="5" width="22" height="19" rx="2"/>
        <line x1="2" y1="10" x2="24" y2="10"/>
        <line x1="8" y1="2" x2="8" y2="7"/><line x1="18" y1="2" x2="18" y2="7"/>
        <path d="M6 14h14M6 18h14M10 12v10M14 12v10M18 12v10" stroke-width="1"/>
      </svg>
      <span>Friday, August 9th, 2019</span>
    </div>
    <span class="divider"></span>
    <div class="detail detail-web">
      <svg width="26" height="26" viewBox="0 0 26 26" fill="none" stroke="#fff" stroke-width="1.6">
        <circle cx="13" cy="13" r="11"/>
        <ellipse cx="13" cy="13" rx="5" ry="11"/>
        <line x1="2" y1="13" x2="24" y2="13"/>
        <path d="M4 7h18M4 19h18"/>
      </svg>
      <span>marcusadrianhollis.com | brightmark.ca</span>
    </div>
  </div>
</div>
</body>
</html>
```